Garden building leaflet A4 tri fold

We need an A4 tri fold (printed both sides) flyer design for a local business based in East Hampshire (UK) called Corrick Yard Buildings.We offer a bespoke garden building service from design, construction, installation and maintenance.Typical use is for home office, garden studio, playrooms, garage workshops, therapy rooms and extra living accommodation. Including connection to all services as required.The final design should stress that this is a local business that has been serving the East Hampshire community for almost 20 years. Over this time Corrick's has built a reputation for quality construction with customer satisfaction the overriding driving force.Over the last 20 years we've seen a huge increase in people working from home at least one day per week and a shift back to family focused lifestyles. Even large multi national companies are promoting home working as it has been shown by recent studies home workers are more productive than solely office based employees. Corrick Yard Buildings is a greener way of working, improves work-life balance and accelerates your productivity.

Target Market(s)

ABC1

Industry/Entity Type

Business

Requirements
Must have
• Pictures/photos of garden office buildings and garden studios in typical UK garden surroundings. Contemporary structures essential with modern building design.
Nice to have
• Internal pictures of people working in a garden room or garden studio environment.

```html
<!DOCTYPE html>
<html lang="en">
<head>
<meta charset="utf-8">
<title>Corrick Yard Buildings – Leaflet</title>
<link rel="stylesheet" href="https://fonts.googleapis.com/css2?family=Archivo:wght@700;800&family=Roboto:wght@400;500;700&display=swap">
<style>
  :root{
    --green-bright:#8ad92a;
    --green-mid:#5cbc17;
    --green-deep:#2f8d10;
    --yellow:#f2f20a;
    --ink:#222222;
    --body-ink:#444444;
    --panel-white:#ffffff;
    --panel-grey:#dcdcdc;
    --page-bg:#e6e6e6;
    --sky:#b9dcf2;
    --lawn:#4f9a2a;
  }
  *{margin:0;padding:0;box-sizing:border-box}
  html,body{width:1200px;height:889px;overflow:hidden;background:var(--page-bg)}
  .leaflet{position:absolute;left:0;top:19px;width:1200px;height:851px;overflow:hidden;font-family:"Roboto",Arial,sans-serif}
  .leaflet-bg{position:absolute;inset:0;width:1200px;height:851px}
  .section-tag{position:absolute;left:4px;width:264px;height:32px;border-radius:0 16px 16px 0;
    background:linear-gradient(#6fd018,var(--green-deep));color:#fff;font-weight:700;font-size:19px;
    letter-spacing:.5px;line-height:32px;padding-left:28px;text-transform:uppercase}
  .tag-quality{top:170px}
  .tag-offer{top:668px}
  .body-copy{position:absolute;left:34px;width:366px;font-size:13.4px;line-height:17px;color:var(--body-ink);text-align:justify}
  .body-copy p+p{margin-top:17px}
  .copy-quality{top:232px}
  .copy-offer{top:712px}
  .call-box{position:absolute;left:440px;top:588px;width:330px;height:263px;background:var(--yellow);border-radius:22px 22px 0 0;text-align:center}
  .call-title{margin-top:34px;font-size:31px;font-weight:500;color:var(--green-deep);display:flex;align-items:center;justify-content:center;gap:12px}
  .call-number{font-size:37px;font-weight:500;color:#111;line-height:50px}
  .call-numbers{margin-top:12px}
  .brand-name{position:absolute;left:828px;top:46px;width:350px;text-align:center;font-family:"Archivo",Arial,sans-serif;font-weight:800;font-size:58px;letter-spacing:3px;color:var(--ink)}
  .brand-line{position:absolute;left:830px;top:126px;width:330px;height:44px;border-radius:22px;background:linear-gradient(#ffffff,#cfcfcf);
    text-align:center;line-height:44px;font-size:25px;color:#333;text-transform:uppercase}
  .experience-badge{position:absolute;left:902px;top:287px;width:236px;height:236px;text-align:center;color:#111;display:flex;flex-direction:column;justify-content:center}
  .badge-small{font-size:30px;font-weight:500;line-height:34px}
  .badge-big{font-size:52px;font-weight:700;color:var(--green-deep);line-height:56px}
  .badge-tail{font-size:23px;font-weight:500;line-height:28px}
</style>
</head>
<body>
<main class="leaflet">
  <svg class="leaflet-bg" viewBox="0 0 592 420" preserveAspectRatio="none" aria-hidden="false">
    <defs>
      <linearGradient id="greenField" x1="0" y1="0" x2="1" y2="1">
        <stop offset="0" stop-color="#4fb012"/>
        <stop offset=".5" stop-color="var(--green-bright)"/>
        <stop offset="1" stop-color="#58b514"/>
      </linearGradient>
      <linearGradient id="photoTones" x1="0" y1="0" x2="0" y2="1">
        <stop offset="0" stop-color="var(--sky)"/>
        <stop offset=".45" stop-color="#d9d2c2"/>
        <stop offset=".65" stop-color="#6aa83a"/>
        <stop offset="1" stop-color="var(--lawn)"/>
      </linearGradient>
      <linearGradient id="panelTone" x1="0" y1="0" x2="1" y2="0">
        <stop offset="0" stop-color="var(--panel-grey)"/>
        <stop offset=".5" stop-color="var(--panel-white)"/>
        <stop offset="1" stop-color="#eeeeee"/>
      </linearGradient>
      <clipPath id="innerArea">
        <path d="M0,52 C200,22 410,34 498,130 C555,195 570,330 525,420 L0,420 Z"/>
      </clipPath>
    </defs>
    <rect class="green-field" width="592" height="420" fill="url(#greenField)"/>
    <g clip-path="url(#innerArea)">
      <rect class="garden-photo" role="img" aria-label="Photo of a modern building with a landscaped garden, stone planters and yellow flower beds" x="200" y="0" width="392" height="420" fill="url(#photoTones)"/>
      <rect class="text-panel" x="0" y="0" width="200" height="420" fill="url(#panelTone)"/>
    </g>
    <path class="swoosh-dark" d="M0,52 C200,22 410,34 498,130 C555,195 570,330 525,420" fill="none" stroke="var(--green-deep)" stroke-width="3"/>
    <path class="swoosh-yellow" d="M0,45 C200,15 416,27 505,124 C563,192 581,330 536,420" fill="none" stroke="var(--yellow)" stroke-width="11"/>
    <circle class="badge-ring" cx="503" cy="200" r="67" fill="var(--yellow)"/>
    <circle class="badge-face" cx="503" cy="200" r="59" fill="#ffffff" stroke="var(--green-mid)" stroke-width="1.5"/>
  </svg>

  <div class="section-tag tag-quality">Quality Service</div>
  <div class="body-copy copy-quality">
    <p>The service we provide is an end to end solution encompassing the location, the environment, your specific needs for the purpose of the structure, materials that are sympathetic to the locality, the services required and how you envisage your space will look and feel.</p>
    <p>Our buildings are exceptional and unrivalled. We source the best quality timber and materials for every stage of our building process right down to the paint systems we use. To this end we are always in the market place ensuring that any improvements in products, techniques and components are implemented by us straight away. We employ skilled craftsmen and a well regarded installation team to finish your building to the very highest of our expected standards.</p>
  </div>

  <div class="section-tag tag-offer">What We Offer</div>
  <div class="body-copy copy-offer">
    <p>We acknowledge that each customer has individual requirements based on their specific needs and as such we are flexible in our approach to design and installation. We are happy to replicate an existing building from an illustration, picture or even a pencil drawing on a napkin.</p>
    <p>Contact us for a no obligation consultation to see how we can make your vision become a reality</p>
  </div>

  <div class="call-box">
    <div class="call-title">
      <svg class="phone-icon" width="30" height="24" viewBox="0 0 30 24" aria-hidden="true">
        <path d="M2 8 C2 3 28 3 28 8 L28 10 L21 10 L21 7 L9 7 L9 10 L2 10 Z" fill="var(--green-deep)"/>
        <path d="M7 12 L23 12 L27 22 L3 22 Z" fill="var(--green-deep)"/>
        <circle cx="15" cy="17" r="3" fill="var(--yellow)"/>
      </svg>
      <span>CALL US</span>
    </div>
    <div class="call-numbers">
      <div class="call-number">01632 960418</div>
      <div class="call-number">07700 900236</div>
    </div>
  </div>

  <div class="brand-name">CORRICK</div>
  <div class="brand-line">Yard Buildings</div>

  <div class="experience-badge">
    <div class="badge-small">ALMOST</div>
    <div class="badge-big">20 YEARS</div>
    <div class="badge-tail">OF EXPERIENCE</div>
  </div>
</main>
</body>
</html>
```